Lantern Advisory Business Cards

We need a new layout for our business cards. We have a logo already. But we might be interested in only using the Lantern portion of the logo. It has been uploaded.

We would like cards that are not overly busy. Clean. Modern. Perhaps a gray color for one side.

On the back, we would like to have the lantern part of the logo and "Step Forward, we stand by you!"

Our business provides medics and safety training for corporate clients. Our website is www.lanternadvisoryllc.example.

Industry/Entity Type

Business

Contact Information for Business Card

We want include name, email address, cell phone, main line number, and website URL on the front. Use the following as an example: Marla Tobin, marla@lanternadvisoryllc.example, 402.318.7264 (cell), 402.947.315, and www.lanternadvisoryllc.example.

Font styles to use
Serif
Sans Serif

Requirements
Must have
• All required information. Back side logo with "Take the leap, we will catch you!"
Nice to have
• If possible, we would like to consider creating a card in a non-standard shape. Perhaps, the shape of a lantern. Just interested in understanding the option.

```html
<!DOCTYPE html>
<html lang="en">
<head>
<meta charset="utf-8">
<title>Lantern Advisory — Business Cards</title>
<link rel="stylesheet" href="https://fonts.googleapis.com/css2?family=Crimson+Text:wght@400&display=swap">
<style>
  :root {
    --backdrop: #e8e5e1;
    --card-white: #ffffff;
    --brand-blue: #0b4f97;
    --band-grey: #4b4b4b;
    --ink-dark: #1f1f1f;
    --ink-soft: #5d6a7a;
    --ink-light: #ffffff;
    --serif: "Crimson Text", Georgia, serif;
  }
  * { box-sizing: border-box; margin: 0; padding: 0; }
  html, body { width: 1200px; height: 443px; overflow: hidden; }
  body { background: var(--backdrop); font-family: var(--serif); position: relative; }

  .card {
    position: absolute;
    top: 72px;
    width: 520px;
    height: 300px;
    border-radius: 28px;
    overflow: hidden;
    box-shadow: 0 6px 18px rgba(0,0,0,.18);
  }
  .card--front { left: 40px; background: var(--card-white); }
  .card--back { left: 640px; background: var(--brand-blue); color: var(--ink-light); }

  /* Front */
  .brand {
    position: absolute; top: 14px; left: 0; right: 0;
    display: flex; flex-direction: column; align-items: center; gap: 6px;
  }
  .brand__dot { width: 40px; height: 40px; border-radius: 50%; background: var(--brand-blue); }
  .brand__name {
    font-size: 28px; line-height: 1; letter-spacing: 1.5px; color: var(--ink-dark);
    text-transform: uppercase; font-weight: 400;
  }
  .tagline {
    position: absolute; top: 96px; left: 0; right: 0; text-align: center;
    font-size: 9px; line-height: 1; letter-spacing: 7px; color: var(--ink-soft); text-transform: uppercase;
  }
  .rule { position: absolute; left: 0; right: 0; height: 3px; background: var(--brand-blue); }
  .rule--top { top: 116px; }
  .rule--bottom { top: 238px; }
  .info-band {
    position: absolute; top: 122px; left: 0; right: 0; height: 113px;
    background: var(--band-grey); color: var(--ink-light);
  }
  .person { position: absolute; left: 0; width: 190px; top: 32px; text-align: center; }
  .person__name { font-size: 21px; line-height: 1.1; }
  .person__role { font-size: 15px; margin-top: 2px; }
  .divider { position: absolute; left: 192px; top: 12px; bottom: 12px; width: 1px; background: var(--ink-light); }
  .contacts { position: absolute; left: 210px; top: 18px; list-style: none; }
  .contacts li { display: flex; align-items: center; gap: 10px; font-size: 15px; height: 26px; }
  .contacts svg { width: 14px; height: 14px; fill: var(--ink-light); flex: none; }
  .web-line {
    position: absolute; top: 252px; left: 0; right: 0;
    display: flex; align-items: center; justify-content: center; gap: 10px;
    font-size: 16px; color: var(--ink-dark);
  }
  .web-line svg { width: 14px; height: 14px; }

  /* Back */
  .back-brand {
    position: absolute; top: 52px; left: 0; right: 0;
    display: flex; flex-direction: column; align-items: center; gap: 12px;
  }
  .back-brand__dot { width: 72px; height: 72px; border-radius: 50%; background: var(--ink-light); }
  .back-brand__name { font-size: 22px; line-height: 1; letter-spacing: 1.5px; text-transform: uppercase; }
  .slogan { position: absolute; top: 196px; left: 0; right: 0; text-align: center; font-size: 21px; }
  .back-url { position: absolute; top: 234px; left: 0; right: 0; text-align: center; font-size: 15px; letter-spacing: .5px; }
</style>
</head>
<body>

<section class="card card--front" aria-label="Business card front">
  <div class="brand">
    <span class="brand__dot"></span>
    <span class="brand__name">Lantern Advisory</span>
  </div>
  <p class="tagline">The Readiness Partners</p>
  <div class="rule rule--top"></div>
  <div class="info-band">
    <div class="person">
      <p class="person__name">Marla Tobin</p>
      <p class="person__role">Designation</p>
    </div>
    <div class="divider"></div>
    <ul class="contacts">
      <li>
        <svg viewBox="0 0 16 16" aria-hidden="true"><path d="M3.5 1.5l2.5 0 1 3.5-1.6 1.2c.8 1.8 2.2 3.2 4 4l1.2-1.6 3.5 1v2.5c0 .9-.8 1.6-1.7 1.5C6.9 13.2 2.8 9.1 2 3.2 1.9 2.3 2.6 1.5 3.5 1.5z"/></svg>
        <span>402.947.315</span>
      </li>
      <li>
        <svg viewBox="0 0 16 16" aria-hidden="true"><path d="M4.5 1h7a1 1 0 0 1 1 1v12a1 1 0 0 1-1 1h-7a1 1 0 0 1-1-1V2a1 1 0 0 1 1-1zm.8 2v7h5.4V3zM8 11.5a1 1 0 1 0 0 2 1 1 0 0 0 0-2z"/></svg>
        <span>402.318.7264</span>
      </li>
      <li>
        <svg viewBox="0 0 16 16" aria-hidden="true"><path d="M1 5l7-4 7 4v9H1zm1.6.8L8 9.2l5.4-3.4L8 2.7z"/></svg>
        <span>marla@lanternadvisoryllc.example</span>
      </li>
    </ul>
  </div>
  <div class="rule rule--bottom"></div>
  <div class="web-line">
    <svg viewBox="0 0 16 16" aria-hidden="true"><circle cx="8" cy="8" r="7" fill="#333"/><path d="M1 8h14M8 1c-3 3.5-3 10.5 0 14M8 1c3 3.5 3 10.5 0 14" stroke="#fff" stroke-width="1" fill="none"/></svg>
    <span>www.lanternadvisoryllc.example</span>
  </div>
</section>

<section class="card card--back" aria-label="Business card back">
  <div class="back-brand">
    <span class="back-brand__dot"></span>
    <span class="back-brand__name">Lantern Advisory</span>
  </div>
  <p class="slogan">Step Forward, we stand by you!</p>
  <p class="back-url">www.lanternadvisoryllc.example</p>
</section>

</body>
</html>
```